Lomi-Seret - Promote and Support a community

Design a website for Ethiopean Community. the design should be friendly, easy to navigate and maintain the look & feel of the Ethiopian culture. a proposed logo is attached but it can be change according to your recommendations. This is a project we are doing at a discount rate as it supports a weak community.
Please visit their current website http://www.lomi-seret.example.il/index.php?lang=en

Target Market(s)

Community members, potential doners

Industry/Entity Type

community

Number of Pages Required

1 page

Font styles to use
Sans Serif

Requirements
Must have
• easy to navigate friendly interface

```html
<!DOCTYPE html>
<html lang="en">
<head>
<meta charset="utf-8">
<title>Lomi Seret – Health &amp; Education Presentations</title>
<link href="https://fonts.googleapis.com/css2?family=Lato:wght@400;700;900&display=swap" rel="stylesheet">
<style>
:root{
  --green:#156b36;
  --yellow:#f6c624;
  --ink:#111;
  --muted:#a6a6a6;
  --band:#faf7f4;
  --line:#dcdcdc;
  --photo-a:#6b3a22;
  --photo-b:#c9a27a;
}
*{margin:0;padding:0;box-sizing:border-box}
html,body{width:707px;height:1200px;overflow:hidden;background:#fff}
body{position:relative;font-family:'Lato',sans-serif;color:var(--ink)}
.abs{position:absolute}
.brand{left:94px;top:14px;display:flex;align-items:center;gap:3px;font-size:7px;font-weight:700;color:#b32024}
.brand-dot{width:8px;height:8px;border-radius:50%;background:#b32024}
.nav{left:205px;top:19px;display:flex;gap:12.5px;font-size:6px;font-weight:700}
.nav span{white-space:nowrap}
.btn{background:var(--green);color:#fff;font-weight:700;display:flex;align-items:center;justify-content:center}
.btn-top{left:565px;top:13px;width:68px;height:20px;font-size:6px}
.crumb{left:89px;top:58px;font-size:5.6px;font-weight:700}
.crumb .dim{color:var(--muted);font-weight:400}
.title{left:0;width:707px;top:95px;text-align:center;font-size:18px;font-weight:900}
.body-text{font-size:7.55px;line-height:22.1px}
.p1{left:133px;top:141px;width:222px}
.p2{left:133px;top:338px;width:445px}
.frame{left:356px;top:156px;width:205px;height:129px;background:var(--green)}
.photo{background:linear-gradient(160deg,var(--photo-a),var(--photo-b) 60%,#e8d9c4)}
.hero-photo{left:365px;top:147px;width:205px;height:129px}
.explore{left:0;width:707px;top:707px;text-align:center;font-size:17.5px;font-weight:900}
.brush{left:360px;top:708px;width:83px;height:21px;background:var(--yellow);border-radius:3px 9px 4px 8px}
.card{top:772px;width:128px;height:128px}
.card .photo{height:104px}
.card .label{height:24px;background:var(--yellow);color:#fff;font-size:5.6px;font-weight:900;display:flex;align-items:center;justify-content:center;text-transform:uppercase}
.arrow{top:820px;width:21px;height:21px;border-radius:50%;border:1px solid #e3e3e3;background:#fff;display:flex;align-items:center;justify-content:center}
.band{left:0;top:924px;width:707px;height:102px;background:var(--band);border-top:1px solid var(--line);border-bottom:1px solid var(--line)}
.divider{top:955px;width:1px;height:38px;background:var(--line)}
.partner{background:#e4e4e4}
.footer-rule{left:89px;top:1026px;width:529px;height:1px;background:#ccc}
.fh{font-size:8.6px;font-weight:900}
.ft{font-size:8.4px;line-height:14.3px}
.btn-foot{left:462px;top:1117px;width:83px;height:23px;font-size:7.6px}
</style>
</head>
<body>
<div class="abs brand"><span class="brand-dot"></span>Lomi Seret</div>
<nav class="abs nav">
  <span>HOME</span><span>ABOUT ⌄</span><span>THE COMMUNITY</span><span>PROGRAMS ⌄</span><span>NEWS ⌄</span><span>ADVOCACY</span><span>PARTNERS</span>
</nav>
<div class="abs btn btn-top">SUPPORT US</div>

<div class="abs crumb"><span class="dim">Home &gt; Programs</span> &gt; Health &amp; Education Presentations</div>
<h1 class="abs title">Health &amp; Education Presentations</h1>

<p class="abs body-text p1">To spread awareness of a health promoting lifestyle and an understanding of diabetes and other “lifestyle” chronic diseases, the team of Lomi Seret lecturers deliver presentations to the Ethiopian-Israeli community in Amharic through community centers and clinics, absorption centers, hostels for the elderly, etc.  The presentations have a visual component and the presenter encourages the audience to interact by asking questions and discussing concerns arising from traditional health beliefs or poor understanding.</p>
<div class="abs frame"></div>
<div class="abs photo hero-photo" role="img" aria-label="Audience of elderly community members attending a health lecture"></div>

<div class="abs body-text p2">
<p>Most locations receive a series of lectures covering a range of health topics relevant to the community.  Part of Lomi Seret’s unique approach has been to design a presentation on the importance of physical activity – this lecture is delivered by qualified physical exercise instructors, and uses Ethiopian music and traditional dance movements to help promote regular physical activity as a lifestyle change.  Lomi Seret involves local leaders to provide credibility and influence to their message of health promotion, and conclude meetings with glucose screenings for the audience.  In 2009, over 290 presentations were delivered with an average audience of between 18 to 25 people.</p>
<p>Specially designed educational materials are distributed at the presentations, to reinforce the information delivered through the lectures.  Bearing in mind that 70% of immigrants who left Ethiopia were functionally illiterate in their native Amharic, the materials rely greatly on visual images, using traditional social settings and themes.</p>
<p>Lomi Seret distributes the following educational materials:alt</p>
<p>A short film introducing diabetes and describing why it is a new health concern for Ethiopians now living a western lifestyle in Israel</p>
<p>A short humorous film on the importance of good nutrition and the dangers of obesity, featuring a well known actor from the community A film clip of an exercise lesson given by an Ethiopian-Israeli physical education teacher, accompanied by traditional Ethiopian music An illustrated information leaflet on diabetic foot care featuring traditional figures, specifically for those with poor literacy skills</p>
</div>

<div class="abs brush"></div>
<h2 class="abs explore">Explore are programs</h2>

<div class="abs arrow" style="left:60px"><svg width="8" height="8" viewBox="0 0 8 8"><path d="M5.5 1 2.5 4l3 3" fill="none" stroke="#222" stroke-width="1"/></svg></div>
<div class="abs card" style="left:89px"><div class="photo" role="img" aria-label="Community audience at a presentation"></div><div class="label">Health &amp; Education Presentations</div></div>
<div class="abs card" style="left:223px"><div class="photo" role="img" aria-label="Health checks at a regional fair" style="background:linear-gradient(160deg,#5a4230,#d8cfc4 55%,#c08a5a)"></div><div class="label">Regional Health Fairs</div></div>
<div class="abs card" style="left:356px"><div class="photo" role="img" aria-label="Radio studio with presenter" style="background:linear-gradient(160deg,#8a7a5e,#d6d0c6 50%,#6d5a48)"></div><div class="label">Amharic Radio Program</div></div>
<div class="abs card" style="left:490px"><div class="photo" role="img" aria-label="Women sharing food at a cookery course" style="background:linear-gradient(160deg,#4a5a4a,#2aa39a 55%,#e2c27a)"></div><div class="label">Nutrition &amp; Cookery Courses</div></div>
<div class="abs arrow" style="left:625px"><svg width="8" height="8" viewBox="0 0 8 8"><path d="M2.5 1 5.5 4l-3 3" fill="none" stroke="#222" stroke-width="1"/></svg></div>

<section class="abs band" aria-label="Partners"></section>
<div class="abs partner" style="left:89px;top:959px;width:36px;height:33px"></div>
<div class="abs divider" style="left:149px"></div>
<div class="abs partner" style="left:175px;top:966px;width:56px;height:18px"></div>
<div class="abs divider" style="left:255px"></div>
<div class="abs partner" style="left:282px;top:959px;width:42px;height:33px"></div>
<div class="abs divider" style="left:349px"></div>
<div class="abs partner" style="left:375px;top:959px;width:53px;height:33px"></div>
<div class="abs divider" style="left:455px"></div>
<div class="abs partner" style="left:480px;top:952px;width:32px;height:46px"></div>
<div class="abs divider" style="left:539px"></div>
<div class="abs partner" style="left:563px;top:966px;width:54px;height:20px"></div>
<div class="abs footer-rule"></div>

<div class="abs" style="left:89px;top:1049px">
  <div class="fh">PHONE</div><div class="ft" style="margin-top:1px">04-5550187</div>
  <div class="fh" style="margin-top:14px">OFFICE</div><div class="ft" style="margin-top:1px">Dekel 12/4 POB 4120 Hadera, 38150</div>
  <div class="fh" style="margin-top:14px">E-MAIL</div><div class="ft" style="margin-top:1px">lomiseret@example.org</div>
</div>
<div class="abs" style="left:290px;top:1049px;width:160px">
  <div class="fh">LOMI SERET</div>
  <p class="ft" style="margin-top:2px">Lomi means health in Amharic, and also signifies a jewel basket: an expensive and unique gift to preserve.</p>
  <p class="ft" style="margin-top:14px">Seret means health in Hebrew.</p>
  <p class="ft" style="margin-top:14px">Health is a gift to be preserved</p>
</div>
<div class="abs" style="left:462px;top:1049px;width:160px">
  <div class="fh">ABOUT US</div>
  <p class="ft" style="margin-top:2px">Lomi Seret (“health” in both Amharic and Hebrew) is dedicated to improving the health of the Ethiopian Israeli community.</p>
</div>
<div class="abs btn btn-foot">SUPPORT US</div>
</body>
</html>
```